two-fold brochure design for oral product

Folded dimension: 21cm*9.5 cm, unfolded dimension: 21*19 cm.
CMYK, 300 pixels, ready for printing.
I hope the brochure would be upmarket.
If you need more elements about our products or brand for this design, pls let me know.

Target Market(s)

female from 20-40

```html
<!DOCTYPE html>
<html lang="en">
<head>
<meta charset="utf-8">
<title>Protect and Nourish – Oral Care Essence Brochure</title>
<link href="https://fonts.googleapis.com/css2?family=Fredoka:wght@500;600&family=Quicksand:wght@500;600&display=swap" rel="stylesheet">
<style>
  :root {
    --bg: #e3e7c6;
    --bg-light: #eef2d9;
    --olive: #5a6a26;
    --olive-soft: #6e8030;
    --ink: #2e3320;
    --mint: #9fcfb8;
    --mint-deep: #86c0a6;
    --pink: #f0a2bc;
    --bottle: #4a5a26;
  }
  * { margin: 0; padding: 0; box-sizing: border-box; }
  html, body { width: 1089px; height: 1200px; overflow: hidden; }
  body {
    position: relative;
    background: var(--bg);
    font-family: "Quicksand", sans-serif;
    color: var(--ink);
  }
  .left-panel-glow {
    position: absolute; left: 0; top: 0; width: 545px; height: 1104px;
    background: radial-gradient(ellipse at 30% 20%, var(--bg-light) 0%, var(--bg) 70%);
  }
  .product-photo {
    position: absolute; left: 0; top: 0; width: 380px; height: 560px;
    background: linear-gradient(155deg, var(--bottle) 0%, #5e6e30 45%, #c9d0a8 78%, rgba(227,231,198,0) 100%);
    border-bottom-right-radius: 120px;
  }
  .heading {
    font-family: "Fredoka", sans-serif;
    font-weight: 600;
    color: var(--olive);
    line-height: 1;
  }
  .reasons-title {
    position: absolute; left: 68px; top: 446px;
    font-size: 50px; line-height: 52px;
  }
  .reasons {
    position: absolute; left: 66px; top: 566px; width: 382px;
  }
  .item-title {
    font-family: "Fredoka", sans-serif;
    font-weight: 600;
    color: var(--olive-soft);
    font-size: 21px; line-height: 28px;
  }
  .item-text {
    font-size: 20px; line-height: 28.2px; font-weight: 500;
    text-align: justify;
  }
  .reasons .item + .item { margin-top: 4px; }
  .flora {
    position: absolute; left: 33px; top: 952px; width: 502px; height: 152px;
    background: linear-gradient(180deg, rgba(90,106,38,0) 0%, rgba(90,106,38,0.18) 100%);
    border-radius: 40px 40px 0 0;
  }
  .howto-title {
    position: absolute; left: 567px; top: 42px;
    font-size: 54px;
  }
  .step-photo {
    position: absolute; left: 564px; width: 175px;
    background: linear-gradient(160deg, var(--mint) 0%, var(--mint-deep) 100%);
  }
  .step-photo.daily { top: 120px; height: 226px; }
  .step-photo.topical { top: 514px; height: 181px; left: 563px; width: 176px; }
  .step-photo.special { top: 863px; height: 207px; }
  .step {
    position: absolute; left: 751px; width: 283px;
  }
  .step.daily { top: 115px; }
  .step.topical { top: 511px; width: 292px; }
  .step.special { top: 859px; width: 269px; }
  .band {
    position: absolute; left: 0; top: 1104px; width: 1089px; height: 96px;
    background: var(--pink);
    display: flex; align-items: center; justify-content: center;
  }
  .tagline {
    font-family: "Fredoka", sans-serif; font-weight: 600;
    color: var(--olive); font-size: 38px; letter-spacing: 0.36em;
    padding-left: 0.36em;
  }
</style>
</head>
<body>
  <div class="left-panel-glow"></div>
  <div class="product-photo" role="img" aria-label="Photo of a dark green essence bottle pouring a clear drop"></div>

  <h1 class="heading reasons-title">Reasons<br>to choose:</h1>
  <section class="reasons">
    <div class="item">
      <h3 class="item-title">Freshen breath</h3>
      <p class="item-text">Effectively inhibit the growth of harmful bacteria in the mouth, improve oral health, and get rid of odor.</p>
    </div>
    <div class="item">
      <h3 class="item-title">Nourish and repair</h3>
      <p class="item-text">Improve immunity, so that the damaged oral epidermis and gum tissue can be repaired in time.</p>
    </div>
    <div class="item">
      <h3 class="item-title">Soothe discomfort</h3>
      <p class="item-text">Harnesses the natural properties of herbs to reduce the sensitivity of the pain nerves in the mouth.</p>
    </div>
  </section>
  <div class="flora" role="img" aria-label="Line illustration of wild herbs and flowers"></div>

  <h2 class="heading howto-title">How to use:</h2>

  <div class="step-photo daily" role="img" aria-label="Dropper adding essence onto toothpaste on a toothbrush"></div>
  <div class="step daily">
    <h3 class="item-title">Daily oral care</h3>
    <p class="item-text">Brush your teeth with drops on top of toothpaste<br>Squeeze the toothpaste onto the toothbrush first, then put a drop of essence on the toothpaste and brush your teeth thoroughly for at least three minutes</p>
  </div>

  <div class="step-photo topical" role="img" aria-label="Dropper applying essence to a dental model"></div>
  <div class="step topical">
    <h3 class="item-title">Topical oral care</h3>
    <p class="item-text">Drop and penetrate between the teeth<br>Drop the essence between your teeth or on the uncomfortable area, do not rinse your mouth after dripping, and do not drink water for half an hour.</p>
  </div>

  <div class="step-photo special" role="img" aria-label="Dropper applying essence into a clear retainer"></div>
  <div class="step special">
    <h3 class="item-title">Special oral care</h3>
    <p class="item-text">Drop in braces and wear<br>Remove the invisible braces or clear retainers, and drip gum essence into the braces to wear.</p>
  </div>

  <footer class="band">
    <p class="tagline">PROTECT AND NOURISH</p>
  </footer>
</body>
</html>
```